Luxury Wine Label for New Startup Winery

We need a wine label for our new winery startup. We have worked with a local designer but do not feel the resulting label / logo have the elevation required to present our brand as a luxury wine. Our winery is called "Harrowgate Vineyards" and we are focused on extremely high quality hand crafted artisan and estate wines from the Pacific Northwest.
We would like to see designs that utilize a tree line, or other imagery that represents the "Harrowgate" part of our company name. Another interesting feature could be wood grain.
A logo will be required based on your design so please design with this in mind:
This logo should be consistent with the wine bottle label design, and should be representative of our high end exclusive wine while giving a sense of place (Oregon/ Pacific Northwest.)
I will supply an image of the design we received from our local designer, PLEASE NOTE: in general we do like wood grain and tree line concepts but feel the execution was poorly done.
ATTN: Logo design should be suitable for use on: Bottles (Red wine/rose/white wine), Bussiness cards, vehicle signage, business signage, etc
P.S.:
If you have a design that is not outside the box we are still interested in seeing it.
Label is for a burgundy style bottle with a label height of 3.5 - 4" and a width of 3.5-4"
any label <= 4"x4" and >=3.5"x3.5" will be acceptable:
HOWEVER Width should be greater than or equal to height due to the bottle format
Target Market(s)
Wine enthusiasts with adequate discretionary budgets to afford $100 bottles of wine.
Industry/Entity Type
Wine / Winery
Requirements
Must have
- A sense of luxury, a feel of exclusivity, and a theme consistent with our product and brand name
Nice to have
- Tree line, wood grain or other wood themes. Serif fonts
Should not have
- anything cheesy, off topic, hard to read script fonts or anything that makes the label hard to read from a few feet away or too busy

```html
<!DOCTYPE html>
<html lang="en">
<head>
<meta charset="utf-8">
<title>Harrowgate Vineyards – Red Wine Label</title>
<link rel="stylesheet" href="https://fonts.googleapis.com/css2?family=Cinzel:wght@500;600&family=Oswald:wght@500&display=swap">
<style>
  :root {
    --page-bg: #ffffff;
    --wood-light: #5a463a;
    --wood-mid: #4d3b30;
    --wood-dark: #3e2f26;
    --gold: #dcc28a;
    --gold-soft: #c9ad74;
  }
  html, body {
    margin: 0;
    padding: 0;
    width: 1200px;
    height: 1200px;
    overflow: hidden;
    background: var(--page-bg);
  }
  .canvas {
    position: relative;
    width: 1200px;
    height: 1200px;
  }
  .label {
    position: absolute;
    left: 100px;
    top: 150px;
    width: 1000px;
    height: 900px;
  }
  .label-art {
    position: absolute;
    inset: 0;
  }
  .winery-name {
    position: absolute;
    left: 0;
    width: 1000px;
    top: 200px;
    margin: 0;
    text-align: center;
    font-family: "Cinzel", serif;
    font-weight: 600;
    font-size: 50px;
    line-height: 60px;
    letter-spacing: 1px;
    color: var(--gold);
  }
  .wine-type {
    position: absolute;
    left: 0;
    width: 1000px;
    top: 395px;
    margin: 0;
    text-align: center;
    font-family: "Oswald", sans-serif;
    font-weight: 500;
    font-size: 104px;
    line-height: 130px;
    color: var(--gold);
  }
</style>
</head>
<body>
<main class="canvas">
  <section class="label">
    <svg class="label-art" width="1000" height="900" viewBox="0 0 1000 900">
      <defs>
        <linearGradient id="woodTone" x1="0" y1="0" x2="1" y2="1">
          <stop offset="0" stop-color="var(--wood-light)"/>
          <stop offset="0.5" stop-color="var(--wood-mid)"/>
          <stop offset="1" stop-color="var(--wood-dark)"/>
        </linearGradient>
        <linearGradient id="treeTone" x1="0" y1="0" x2="0" y2="1">
          <stop offset="0" stop-color="var(--gold)" stop-opacity="0.15"/>
          <stop offset="0.45" stop-color="var(--gold)" stop-opacity="0.6"/>
          <stop offset="1" stop-color="var(--gold)" stop-opacity="0.9"/>
        </linearGradient>
        <linearGradient id="flourishTone" x1="0" y1="0" x2="1" y2="0">
          <stop offset="0" stop-color="var(--gold-soft)" stop-opacity="0"/>
          <stop offset="0.5" stop-color="var(--gold-soft)" stop-opacity="0.55"/>
          <stop offset="1" stop-color="var(--gold-soft)" stop-opacity="0"/>
        </linearGradient>
      </defs>

      <rect class="label-body" x="0" y="0" width="1000" height="900" rx="18"
            fill="url(#woodTone)" role="img" aria-label="Dark walnut wood grain label background"/>

      <path class="frame-outer"
            d="M278,125 L722,125 A28,28 0 0 0 750,153 L750,747 A28,28 0 0 0 722,775 L278,775 A28,28 0 0 0 250,747 L250,153 A28,28 0 0 0 278,125 Z"
            fill="none" stroke="var(--gold)" stroke-width="5"/>
      <path class="frame-inner"
            d="M286,137 L714,137 A24,24 0 0 0 738,161 L738,739 A24,24 0 0 0 714,763 L286,763 A24,24 0 0 0 262,739 L262,161 A24,24 0 0 0 286,137 Z"
            fill="none" stroke="var(--gold)" stroke-width="2"/>

      <ellipse class="flourish flourish-top" cx="500" cy="345" rx="150" ry="12"
               fill="url(#flourishTone)" role="img" aria-label="Gold scroll flourish"/>
      <ellipse class="flourish flourish-bottom" cx="500" cy="538" rx="150" ry="12"
               fill="url(#flourishTone)" role="img" aria-label="Gold scroll flourish"/>

      <rect class="tree-line" x="320" y="610" width="360" height="140" rx="10"
            fill="url(#treeTone)" role="img" aria-label="Gold silhouette of an evergreen tree line"/>
    </svg>
    <h1 class="winery-name">Harrowgate<br>Vineyards</h1>
    <p class="wine-type">RED WINE</p>
  </section>
</main>
</body>
</html>
```